Business Card Design Project

A business card for a new company in Ontario Canada called Build for Growth. It is a consulting company which uses Brixo as the medium for facilitation.

The target market is for senior leaders in healthcare and social services.

Industry/Entity Type

Healthcare

Requirements
Must have
• The name Build For Growth
Dana Montreuil RRT, B Ed (AD ed).
Tacticraft Facililitator (R)

Tag Line
Engaging Transforming and Innovative
The attached logo

danamontreuil@examplemail.com
416-555-0147
Should not have
• Lime green
Times New Roman or Arial font
Do not include Brixo bricks on the card.

```html
<!DOCTYPE html>
<html lang="en">
<head>
<meta charset="utf-8">
<title>Build for Growth – Dana Montreuil</title>
<link rel="stylesheet" href="https://fonts.googleapis.com/css2?family=Comic+Neue:ital,wght@0,400;0,700;1,400;1,700&family=Roboto:wght@300&display=swap">
<style>
  :root {
    --sky: #4fd6fb;
    --violet: #4a14f0;
    --teal: #12a89a;
    --magenta: #ef2fc8;
    --slate: #5c6668;
    --mist: #d5dcdc;
    --paper: #ffffff;
  }
  html, body {
    margin: 0;
    padding: 0;
    overflow: hidden;
    background: var(--paper);
  }
  .card {
    position: relative;
    width: 1200px;
    height: 790px;
    overflow: hidden;
    background: var(--paper);
    font-family: "Comic Neue", "Comic Sans MS", cursive;
  }
  .card-backdrop {
    position: absolute;
    inset: 0;
    width: 1200px;
    height: 790px;
  }
  .logo-panel {
    position: absolute;
    left: 86px;
    top: 17px;
    width: 383px;
    height: 370px;
    background: linear-gradient(180deg, #ffffff 0%, #ffffff 70%, #e6e6e6 100%);
    box-shadow: 2px 4px 8px rgba(0, 0, 0, 0.35);
    display: flex;
    flex-direction: column;
    align-items: center;
    justify-content: flex-end;
    padding-bottom: 26px;
    box-sizing: border-box;
  }
  .logo-mark {
    width: 200px;
    height: 200px;
    background: var(--violet);
    margin-bottom: 44px;
  }
  .logo-name {
    font-weight: 700;
    font-size: 27px;
    letter-spacing: 1px;
    color: #1a1a1a;
    text-transform: uppercase;
  }
  .tagline {
    position: absolute;
    left: 592px;
    top: 144px;
    margin: 0;
    font-weight: 700;
    font-size: 31px;
    letter-spacing: 0.3px;
    white-space: nowrap;
  }
  .tagline .word-engaging { color: var(--violet); }
  .tagline .word-transforming { color: var(--sky); }
  .tagline .word-and { color: var(--teal); }
  .tagline .word-innovative { color: var(--magenta); }
  .contact {
    position: absolute;
    right: 96px;
    top: 402px;
    text-align: right;
    white-space: nowrap;
  }
  .person-name {
    margin: 0;
    font-size: 58px;
    line-height: 1;
    font-weight: 700;
  }
  .person-name .first { color: var(--violet); }
  .person-name .last { color: var(--sky); font-style: italic; font-weight: 400; }
  .person-credentials {
    margin: 6px 0 0;
    font-family: "Roboto", "Helvetica Neue", sans-serif;
    font-weight: 300;
    font-size: 22px;
    color: var(--slate);
  }
  .person-role {
    margin: 2px 0 0;
    font-family: "Roboto", "Helvetica Neue", sans-serif;
    font-weight: 300;
    font-size: 28px;
    color: var(--sky);
  }
  .person-phone,
  .person-email {
    margin: 0;
    font-weight: 700;
    font-size: 35px;
    line-height: 1.2;
    color: var(--slate);
  }
  .person-phone { margin-top: 12px; }
</style>
</head>
<body>
  <div class="card">
    <svg class="card-backdrop" viewBox="0 0 1063 700" preserveAspectRatio="none" aria-hidden="true">
      <rect x="0" y="15" width="1063" height="600" fill="var(--sky)"/>
      <path d="M0,300 C40,190 220,105 430,95 C650,86 900,82 1063,72 L1063,620 L0,620 Z" fill="var(--violet)"/>
      <path d="M0,480 C10,260 200,135 430,118 C650,104 900,104 1063,98 L1063,620 L0,620 Z" fill="var(--paper)"/>
      <path d="M0,545 C260,605 620,625 1063,582 L1063,700 L0,700 Z" fill="var(--mist)"/>
      <path d="M0,650 C380,652 760,630 1063,592 L1063,700 L0,700 Z" fill="var(--paper)"/>
      <path d="M0,672 C400,668 800,655 1063,640 L1063,700 L0,700 Z" fill="var(--violet)"/>
    </svg>

    <div class="logo-panel">
      <div class="logo-mark"></div>
      <div class="logo-name">Build for Growth</div>
    </div>

    <p class="tagline">
      <span class="word-engaging">Engaging</span>
      <span class="word-transforming">Transforming</span>
      <span class="word-and">and</span>
      <span class="word-innovative">Innovative</span>
    </p>

    <div class="contact">
      <h1 class="person-name"><span class="first">Dana</span> <span class="last">Montreuil</span></h1>
      <p class="person-credentials">RRT, B Ed (AD ed)</p>
      <p class="person-role">Tacticraft Facililitator (R)</p>
      <p class="person-phone">416-555-0147</p>
      <p class="person-email">danamontreuil@examplemail.com</p>
    </div>
  </div>
</body>
</html>
```